Commercial Security Landing Page

We're looking for a simple customizable Bootstrap based single landing page similar to http://gridtemplex.net/preview/GT482K913

I have attached our Full Logo to incorporate into the design.
I can also attach other assets if required.

We're in the Commercial Security Industry, we specialize in (These must be included on the site):
- CCTV
- Access Control
- Automation
- Fire Monitoring
- Theft Protection/Burglar Alarms

More information:
We install these systems in customers businesses to protect them from theft, fire, etc. We do very high quality installs and only use the highest quality equipment for each customer. We do not do network security or anything like that, we focus completely in protecting businesses and homes through the use of CCTV, Access Control, Automation such as (light control, garage control, flood protection, etc), we also handle fire monitoring, theft protection, and burglar alarms.

Specs/Requirements:
- Must not be built with WordPress.
- Must be built using Twitter Bootstrap
- Any images used must not be copyright protected or contain royalties.
- Eye Catching Stock Photos or Placeholder so that we can replace with our own photos.
- SEO Friendly
- Easily adjustable
- Contains a contact form
- Customized to our industry.
- Must be "modern" and scalable across all devices.

Colors we like:
- #0C9ED9
- #595A5C
- #414142

Target Market(s)

Business Owners, Home Owners, Enterprise

Industry/Entity Type

Security Service

Coding

Coded - Design and coding required

Font styles to use
Sans Serif

Requirements
Must have
• Must contain highlights of the following bullet points:
• - CCTV
• - Access Control
• - Automation
• - Fire Monitoring
• - Theft Protection/Burglar Alarms
Nice to have
• - Twitter Bootstrap
• - Any images used must not be copyright protected or contain royalties.
• - Eye Catching Stock Photos or Placeholder so that we can replace with our own photos.
• - SEO Friendly
• Partner Section (Showing off our partners):
• Vexlo.net (https://www.vexlo.net/)
• Tarnel Gate (http://www.tarnelgate.net/)
• BQM (http://www.brenwickquillmoor.net/)
Should not have
• Should not be built on Wordpress

```html
<!DOCTYPE html>
<html lang="en">
<head>
<meta charset="utf-8">
<title>Ravolin – Commercial Security</title>
<link href="https://fonts.googleapis.com/css2?family=Poppins:wght@300;400;500;600&family=Barlow+Semi+Condensed:wght@400;500;600&display=swap" rel="stylesheet">
<style>
:root{
  --blue:#0C9ED9;
  --grey:#595A5C;
  --dark:#414142;
  --ink:#2b2b2c;
  --footer:#1b1b1b;
  --field:#2a2a2a;
  --white:#ffffff;
}
*{margin:0;padding:0;box-sizing:border-box}
html,body{width:1200px;height:3169px;overflow:hidden;background:var(--white)}
body{font-family:'Poppins',sans-serif;color:var(--grey);position:relative}
.abs{position:absolute}
.head-font{font-family:'Barlow Semi Condensed','Poppins',sans-serif}

/* nav */
.topbar{top:0;left:0;width:1200px;height:70px;background:var(--white);border-top:4px solid #e4e4e4}
.brand{left:112px;top:14px;display:flex;align-items:center;gap:8px;font-size:30px;font-weight:600;color:var(--blue);letter-spacing:1px}
.brand-mark{width:34px;height:34px;border:3px solid var(--blue);border-radius:9px}
.nav{top:20px;left:548px;display:flex;gap:0;font-size:13px;color:var(--dark)}
.nav a{display:block;width:120px;text-align:center;line-height:32px;color:var(--dark);text-decoration:none}
.nav a.active{width:80px;margin-right:20px;border:1px solid var(--blue);border-radius:4px;color:var(--blue)}

/* hero */
.hero{top:70px;left:0;width:1200px;height:598px;background:radial-gradient(ellipse at 72% 40%,#7a7d84 0%,#4c4f55 35%,#2f3136 70%,#26282c 100%)}
.hero-frame{left:118px;top:118px;width:426px;height:334px}
.hero-copy{left:130px;top:190px;width:400px;text-align:center;color:var(--white)}
.hero-copy h1{font-weight:400;font-size:56px;line-height:64px}
.hero-copy p{color:var(--blue);font-size:28px;margin-top:20px;letter-spacing:.5px}

/* section heading */
.sec-title{left:0;width:1200px;text-align:center;font-size:36px;color:var(--blue)}
.rule{left:380px;width:440px;height:1px;background:#d5d5d5}
.rule::after{content:"";position:absolute;left:214px;top:0;border-left:6px solid transparent;border-right:6px solid transparent;border-top:6px solid var(--blue)}
.rule.light{background:rgba(255,255,255,.7)}
.rule.light::after{border-top-color:var(--white)}
.lead{left:130px;width:940px;text-align:center;font-size:11.5px;line-height:21px;color:var(--grey)}

/* welcome */
.welcome-title{top:748px;left:0;width:1200px;display:flex;justify-content:center;align-items:center;gap:10px;font-size:34px;color:var(--dark)}
.welcome-title b{color:var(--blue);font-weight:600;letter-spacing:1px}
.more{left:543px;top:940px;width:80px;height:30px;border:1.5px solid var(--blue);border-radius:5px;font-size:11px;font-weight:600;color:var(--blue);text-align:center;line-height:27px}

/* services */
.services{top:1048px;left:0;width:1200px;height:386px;background:linear-gradient(100deg,#139fd9 0%,#0C9ED9 55%,#2aa7dc 80%,#1897d0 100%)}
.service{width:160px;text-align:center;color:var(--white)}
.service .icon{width:84px;height:64px;margin:0 auto;border:3px solid var(--white);border-radius:12px;display:flex;align-items:center;justify-content:center}
.service h3{font-family:'Barlow Semi Condensed','Poppins',sans-serif;font-weight:500;font-size:19px;margin-top:20px}

/* clients */
.clients-copy{left:113px;top:1600px;width:385px;font-size:11.5px;line-height:21.5px}
.partner{top:1645px;display:flex;align-items:center;gap:8px;font-size:22px;font-weight:600;color:var(--dark)}
.partner i{display:block;width:18px;height:18px;background:var(--dark)}

/* testimonial */
.quote-band{top:1805px;left:0;width:1200px;height:265px;background:linear-gradient(90deg,#5a5b5d,#727376 50%,#5c5d60)}
.quote{left:135px;top:1883px;width:960px;font-size:13px;line-height:24px;color:var(--white)}
.quote-by{left:800px;top:1968px;width:260px;text-align:right;font-size:13px;color:var(--white)}

/* blog */
.post{top:2228px;width:312px}
.post-head{display:flex;gap:12px;height:44px}
.date{width:36px;height:44px;background:var(--blue);color:var(--white);text-align:center;font-size:11px;line-height:13px;padding-top:5px}
.date b{display:block;font-size:16px;line-height:18px}
.post h3{font-size:14px;font-weight:500;line-height:21px;color:var(--ink)}
.post-img{margin-top:20px;width:312px;height:146px}
.post p{margin-top:12px;font-size:11.5px;line-height:21.5px}

/* contact */
.contact{top:2598px;left:0;width:1200px;height:571px;background:var(--footer)}
.contact-title{top:2636px;left:0;width:1200px;text-align:center;font-size:30px;color:var(--white)}
.contact-lead{top:2690px;left:200px;width:800px;text-align:center;font-size:12.5px;line-height:26px;color:var(--white)}
.contact-lead a{color:var(--blue);text-decoration:none}
.info{left:113px;color:var(--white);font-size:13px;display:flex;gap:14px}
.dots{left:113px;width:420px;height:8px}
.social{top:2935px;left:205px;display:flex;gap:14px}
.social span{display:block;width:44px;height:44px;border-radius:50%;background:#c7c7c7}
.copy{left:113px;top:3052px;font-size:11.5px;color:var(--white)}
.field{left:568px;width:410px;background:var(--field);color:#8a8a8a;font-size:11px;padding:0 16px;line-height:40px}
.submit{left:849px;top:3033px;width:130px;height:42px;background:var(--blue);color:var(--white);font-size:13px;font-weight:600;text-align:center;line-height:42px}
</style>
</head>
<body>

<header class="abs topbar">
  <div class="abs brand"><span class="brand-mark"></span>Ravolin</div>
  <nav class="abs nav">
    <a class="active" href="#">Home</a><a href="#">About</a><a href="#">Services</a><a href="#">Blog</a><a href="#">Contact</a>
  </nav>
</header>

<section class="abs hero" role="img" aria-label="Close-up photo of a security camera, darkened"></section>
<svg class="abs hero-frame" viewBox="0 0 426 334" aria-hidden="true">
  <path d="M60 4 H380 Q420 4 420 44 V300 Q420 328 392 328 H40 Q6 328 6 294 V60 Q6 4 60 4Z" fill="rgba(20,22,26,.55)" stroke="#0C9ED9" stroke-width="3"/>
  <path d="M70 14 H372 Q410 14 410 52 V288 Q410 318 380 318 H52 Q16 318 16 282 V68 Q16 14 70 14Z" fill="none" stroke="#0C9ED9" stroke-width="2"/>
</svg>
<div class="abs hero-copy">
  <h1>Professional<br>&amp; Powerful</h1>
  <p>SECURITY PROTECTION</p>
</div>

<div class="abs welcome-title head-font"><span class="brand-mark"></span>Welcome to <b>Ravolin</b></div>
<div class="abs rule" style="top:803px"></div>
<p class="abs lead" style="top:826px">Welcome enim ad minim veniam, quis nostrud exercitation ullamco laboris nisi ut aliquip ex ea commodo consequat. Duis aute irure dolor in reprehenderit in voluptate velit esse cillum dolore eu fugiat nulla pariatur. Excepteur sint occaecat cupidatat non proident, sunt Duis aute irure dolor in reprehenderit in voluptate velit esse cillum dolore eu fugiat nulla pariatur in culpa qui officia deserunt mollitanim id . Duis aute irure dolor in reprehenderit in voluptate velit esse cillum dolore eu fugiat nulla pariatur in culpa qui officia deserunt mollitanim id est laborum</p>
<div class="abs more">MORE</div>

<section class="abs services" role="img" aria-label="Blue-tinted photo of an access control keypad"></section>
<h2 class="abs sec-title head-font" style="top:1095px;color:var(--white);font-weight:400">Our Services</h2>
<div class="abs rule light" style="top:1150px"></div>
<p class="abs lead" style="top:1175px;color:var(--white)">Welcome enim ad minim veniam, quis nostrud exercitation ullamco laboris nisi ut aliquip ex ea commodo consequat. Duis aute irure dolor in reprehenderit in voluptate velit esse cillum dolore eu fugiat nulla pariatur. Excepteur sint occaecat .</p>

<div class="abs service" style="left:118px;top:1256px">
  <div class="icon"><svg width="34" height="28" viewBox="0 0 34 28"><path d="M3 6 H31 V10 H3Z M5 10 Q17 30 29 10Z" fill="#fff"/><circle cx="17" cy="15" r="4" fill="#0C9ED9"/></svg></div>
  <h3>CCTV</h3>
</div>
<div class="abs service" style="left:323px;top:1256px">
  <div class="icon"><svg width="30" height="34" viewBox="0 0 30 34"><rect x="3" y="2" width="22" height="30" rx="3" fill="none" stroke="#fff" stroke-width="2.5"/><rect x="8" y="7" width="12" height="6" fill="#fff"/><g fill="#fff"><rect x="8" y="17" width="3" height="3"/><rect x="13" y="17" width="3" height="3"/><rect x="18" y="17" width="3" height="3"/><rect x="8" y="23" width="3" height="3"/><rect x="13" y="23" width="3" height="3"/><rect x="18" y="23" width="3" height="3"/></g></svg></div>
  <h3>Access Control</h3>
</div>
<div class="abs service" style="left:520px;top:1256px">
  <div class="icon"><svg width="32" height="32" viewBox="0 0 32 32"><circle cx="16" cy="16" r="9" fill="none" stroke="#fff" stroke-width="5" stroke-dasharray="4 3"/><circle cx="16" cy="16" r="3" fill="#fff"/></svg></div>
  <h3>Automation</h3>
</div>
<div class="abs service" style="left:720px;top:1256px">
  <div class="icon"><svg width="26" height="32" viewBox="0 0 26 32"><path d="M13 2 C15 10 24 13 22 22 C21 28 17 30 13 30 C8 30 4 27 4 21 C4 15 9 13 9 7 C12 10 12 13 13 15 C15 11 14 6 13 2Z" fill="#fff"/></svg></div>
  <h3>Fire Monitoring</h3>
</div>
<div class="abs service" style="left:913px;top:1256px">
  <div class="icon"><svg width="30" height="32" viewBox="0 0 30 32"><path d="M8 4 H22 L24 12 H6Z" fill="#fff"/><rect x="4" y="12" width="22" height="3" fill="#fff"/><path d="M7 16 H23 V30 H7Z" fill="#fff"/><rect x="10" y="19" width="10" height="2" fill="#0C9ED9"/></svg></div>
  <h3>Theft Protection</h3>
</div>

<h2 class="abs sec-title head-font" style="top:1490px;font-weight:400">Our Clients</h2>
<div class="abs rule" style="top:1545px"></div>
<p class="abs clients-copy">Welcome enim ad minim veniam, quis nostrud exercitation ullamco laboris nisi ut aliquip ex ea commo consequat. Duis aute irure dolor in reprehenderit in voluptate velit esse cillum dolore eu fugiat nulla pariatur. Excepteur sint occaecat cupidatat non. enim ad minim veniam, quis nostrud exercitation ullamco laboris nisi ut aliquip ex ea commo consequat.</p>
<div class="abs partner" style="left:570px"><i></i>Vexlo.net</div>
<div class="abs partner" style="left:820px"><i></i>Tarnel Gate</div>
<div class="abs partner" style="left:1015px">BQM</div>

<section class="abs quote-band" role="img" aria-label="Grey photo of a hand on a concrete wall"></section>
<svg class="abs" style="left:98px;top:1916px" width="14" height="20" viewBox="0 0 14 20"><path d="M11 2 L3 10 L11 18" fill="none" stroke="#fff" stroke-width="3"/></svg>
<svg class="abs" style="left:1086px;top:1916px" width="14" height="20" viewBox="0 0 14 20"><path d="M3 2 L11 10 L3 18" fill="none" stroke="#fff" stroke-width="3"/></svg>
<p class="abs quote">" Lorem ipsum dolor sit amet, consectetuer adipiscing elit, sed diam nonummy nibh euismod tincidunt ut laoreet dolore magna aliquam erat volutpat. Ut wisi enim ad minim veniam, quis nostrud exerci tation ullamcorper suscipit lobortis nisl ut aliquip ex ea commodo consequat. Duis autem vel . Ilamcorper suscipit lobortis nisl ut aliquip ex ea commodo consequat"</p>
<p class="abs quote-by">~ Ipsum Dolor Name</p>

<h2 class="abs sec-title head-font" style="top:2125px;font-weight:400">From the Blog</h2>
<div class="abs rule" style="top:2195px"></div>

<article class="abs post" style="left:113px">
  <div class="post-head"><div class="date"><b>10</b>Dec</div><h3>Nonummy nibh euismod tincidunt ut laoreet dolore magna</h3></div>
  <div class="post-img" role="img" aria-label="Photo of a key in a door lock" style="background:linear-gradient(120deg,#e9e9e9,#8c8c8c 50%,#2f2f2f)"></div>
  <p>Sed diam nonummy nibh euismod tincidunt ut laoreet dolore magna aliquam erat volutpat enim ad minim veniam quis nostrud exerci tatullamco suscipit lobortis nisl ut aliquip...</p>
</article>
<article class="abs post" style="left:446px">
  <div class="post-head"><div class="date"><b>10</b>Dec</div><h3>Nonummy nibh euismod tincidunt ut laoreet dolore magna</h3></div>
  <div class="post-img" role="img" aria-label="Photo of hands holding a globe" style="background:radial-gradient(circle at 50% 50%,#b0706a,#6e3b34 45%,#1f2d52 100%)"></div>
  <p>Sed diam nonummy nibh euismod tincidunt ut laoreet dolore magna aliquam erat volutpat enim ad minim veniam quis nostrud exerci tatullamco suscipit lobortis nisl ut aliquip...</p>
</article>
<article class="abs post" style="left:780px">
  <div class="post-head"><div class="date"><b>10</b>Dec</div><h3>Nonummy nibh euismod tincidunt ut laoreet dolore magna</h3></div>
  <div class="post-img" role="img" aria-label="Photo of a wall-mounted access control terminal" style="background:linear-gradient(90deg,#9fb5c0,#d7dde0 55%,#eef0f1)"></div>
  <p>Sed diam nonummy nibh euismod tincidunt ut laoreet dolore magna aliquam erat volutpat enim ad minim veniam quis nostrud exerci tatullamco suscipit lobortis nisl ut aliquip...</p>
</article>

<footer class="abs contact"></footer>
<h2 class="abs contact-title head-font" style="font-weight:400">CONTACT INFO</h2>
<p class="abs contact-lead">Still haven't found what you are looking for? Mattis condimentm enimroin eget lacus non quam ultricies sodales sit amet sed <a href="#">info@ravolin.net</a></p>

<div class="abs info" style="top:2776px;font-size:15px">
  <svg width="16" height="16" viewBox="0 0 16 16"><path d="M3 1 L6 1 L7 5 L5 6.5 Q6.5 9.5 9.5 11 L11 9 L15 10 L15 13 Q15 15 13 15 Q1 14 1 3 Q1 1 3 1Z" fill="#fff"/></svg>
  123-456-7890
</div>
<div class="abs info" style="top:2812px;line-height:21px">
  <svg width="14" height="20" viewBox="0 0 14 20"><path d="M7 1 C3 1 1 4 1 7 C1 11 7 18 7 18 C7 18 13 11 13 7 C13 4 11 1 7 1Z" fill="#fff"/><circle cx="7" cy="7" r="2.2" fill="#1b1b1b"/></svg>
  <span>Ravolin Security&nbsp; Solutions dolor lorem ipsum<br>Ut wisi enim ad minim ve quiso<br>nostrud exerc, ullamcorper</span>
</div>
<svg class="abs dots" style="top:2906px" viewBox="0 0 420 8"><line x1="0" y1="4" x2="170" y2="4" stroke="#3a3a3a"/><line x1="250" y1="4" x2="420" y2="4" stroke="#3a3a3a"/><g fill="#777"><circle cx="198" cy="4" r="3"/><circle cx="210" cy="4" r="3"/><circle cx="222" cy="4" r="3"/></g></svg>
<div class="abs social"><span></span><span></span><span></span><span></span></div>
<svg class="abs dots" style="top:3004px" viewBox="0 0 420 8"><line x1="0" y1="4" x2="170" y2="4" stroke="#3a3a3a"/><line x1="250" y1="4" x2="420" y2="4" stroke="#3a3a3a"/><g fill="#777"><circle cx="198" cy="4" r="3"/><circle cx="210" cy="4" r="3"/><circle cx="222" cy="4" r="3"/></g></svg>
<p class="abs copy">© 2017 ravolin. All Rights Reserved.</p>

<div class="abs field" style="top:2782px;height:40px">Your full name</div>
<div class="abs field" style="top:2833px;height:40px">Your email address</div>
<div class="abs field" style="top:2885px;height:120px">What can we help for you?</div>
<div class="abs submit">SUBMIT</div>

</body>
</html>
```